Stationery Design Project

I need a design that is simple, clean and modern, in square style, bold font.
The majority of the design needs to be White and Black with a splash of Red colour.
I would like a design for business cards and letter heads with the following information.
Name, Title, Phone, Fax, Email, Website and company ABN number

Target Market(s)

25 to 65 years old real estate clients

Industry/Entity Type

Business

Requirements
Must have
• All designs must incorporate Company Logo, Name, Title, Phone, Fax, Email, Website and company ABN number

```html
<!DOCTYPE html>
<html lang="en">
<head>
<meta charset="utf-8">
<title>Harbor Crest Real Estate – Business Card</title>
<link rel="stylesheet" href="https://fonts.googleapis.com/css2?family=Open+Sans:wght@400;600;700&display=swap">
<style>
  :root {
    --brand-red: #be1e2d;
    --ink: #231f20;
    --paper: #ffffff;
    --stage: #ececec;
    --muted: #3a3a3a;
    --rule: #555555;
  }
  * { box-sizing: border-box; margin: 0; padding: 0; }
  html, body {
    width: 1200px;
    height: 402px;
    overflow: hidden;
    background: var(--stage);
    font-family: "Open Sans", Arial, sans-serif;
  }
  .card {
    position: absolute;
    top: 54px;
    width: 512px;
    height: 291px;
    overflow: hidden;
    box-shadow: 0 2px 6px rgba(0,0,0,0.25);
  }
  .card-front { left: 67px; background: var(--paper); }
  .card-back  { left: 632px; background: var(--brand-red); }

  /* Front: company name */
  .company-name {
    position: absolute;
    top: 50px;
    left: 0;
    width: 100%;
    text-align: center;
    color: var(--ink);
    font-weight: 700;
    line-height: 1.1;
  }
  .company-name .name-main { display: block; font-size: 38px; letter-spacing: 1px; }
  .company-name .name-sub  { display: block; font-size: 12px; letter-spacing: 8px; margin-top: 10px; }

  /* Front: contact block */
  .contact {
    position: absolute;
    top: 188px;
    left: 0;
    width: 100%;
    display: flex;
    justify-content: center;
    color: var(--muted);
    font-size: 13.5px;
    line-height: 18px;
  }
  .contact-col { padding: 0 11px; }
  .contact-col + .contact-col { border-left: 1px solid var(--rule); }
  .contact-line { display: flex; align-items: center; gap: 5px; white-space: nowrap; }
  .icon { width: 10px; height: 10px; flex: none; }

  /* Front: footer band */
  .footer-band { position: absolute; left: 0; bottom: 0; width: 512px; height: 70px; }
  .holder-name {
    position: absolute;
    bottom: 12px;
    left: 0;
    width: 100%;
    text-align: center;
    color: var(--paper);
    font-size: 15px;
  }
  .holder-name strong { font-weight: 700; }

  /* Back */
  .back-mark {
    position: absolute;
    left: 95px;
    top: 70px;
    width: 150px;
    height: 150px;
    border-radius: 50%;
    background: rgba(255,255,255,0.12);
  }
  .back-name {
    position: absolute;
    left: 95px;
    top: 113px;
    width: 150px;
    text-align: center;
    color: var(--paper);
    font-weight: 700;
    font-size: 26px;
    line-height: 32px;
    letter-spacing: 1px;
  }
  .back-web {
    position: absolute;
    left: 277px;
    top: 133px;
    color: var(--paper);
    font-size: 21px;
  }
  .back-web .domain { color: var(--ink); }
</style>
</head>
<body>

<section class="card card-front">
  <h1 class="company-name">
    <span class="name-main">HARBOR CREST</span>
    <span class="name-sub">REAL ESTATE</span>
  </h1>

  <div class="contact">
    <div class="contact-col">
      <p class="contact-line">
        <svg class="icon" viewBox="0 0 10 10"><path d="M2 0.5 L3.8 2.5 L2.8 3.6 Q4 6 6.4 7.2 L7.5 6.2 L9.5 8 L8 9.5 Q3 9 0.5 2 Z" fill="var(--brand-red)"/></svg>
        123-456-7890
      </p>
      <p class="contact-line">
        <svg class="icon" viewBox="0 0 10 10"><rect x="2.5" y="0.5" width="5" height="3" fill="var(--brand-red)"/><rect x="0.5" y="3.5" width="9" height="4" rx="1" fill="var(--brand-red)"/><rect x="2.5" y="7" width="5" height="2.5" fill="var(--brand-red)"/></svg>
        123-456-7890
      </p>
    </div>
    <div class="contact-col">
      <p class="contact-line">
        <svg class="icon" viewBox="0 0 10 10"><circle cx="5" cy="5" r="5" fill="var(--brand-red)"/><rect x="2.3" y="3.3" width="5.4" height="3.6" fill="none" stroke="#fff" stroke-width="0.8"/><path d="M2.3 3.3 L5 5.5 L7.7 3.3" fill="none" stroke="#fff" stroke-width="0.8"/></svg>
        info@harbormail.com
      </p>
      <p class="contact-line">
        <svg class="icon" viewBox="0 0 10 10"><circle cx="5" cy="5" r="5" fill="var(--brand-red)"/><path d="M0.5 5 H9.5 M5 0.5 Q2.5 5 5 9.5 M5 0.5 Q7.5 5 5 9.5" fill="none" stroke="#fff" stroke-width="0.7"/></svg>
        www.website.com
      </p>
    </div>
    <div class="contact-col">
      <p class="contact-line">Street Name, City Name</p>
      <p class="contact-line">State, City Zip Code 000</p>
    </div>
  </div>

  <svg class="footer-band" viewBox="0 0 512 70" preserveAspectRatio="none">
    <path d="M0 29 Q220 6 470 12 Q220 12 0 35 Z" fill="var(--ink)"/>
    <path d="M0 38 Q260 14 512 22 L512 70 L0 70 Z" fill="var(--brand-red)"/>
  </svg>
  <p class="holder-name"><strong>Your Name,</strong> Title</p>
</section>

<section class="card card-back">
  <div class="back-mark"></div>
  <p class="back-name">HARBOR<br>CREST</p>
  <p class="back-web">www.<span class="domain">website</span>.com</p>
</section>

</body>
</html>
```